Valtor Holidays Revamp Project 2015

We are a inbound Travel and tour operator based in Kuala Lumpur, Malaysia, established since 2010. Need a vibrant, dynamic, interactive and user friendly, we expect a Content management system for self data upload.
We cater to different markets around the world form Gulf, to the Far East.
Europe to Africa. With the minimum budget we give maximum services.
The final design should communicate well with the user and portray our growth.

Here is the reference of what our current website looks like.
www.valtorholidays-example.com.my

Target Market(s)

Far-East, South East Asia, Gulf market.

Industry/Entity Type

Travel

Number of Pages Required

5+ page

Font styles to use
Serif
Sans Serif
Other font styles liked:
• Calibri

Requirements
Must have
• User interaction, User friendly, Payment integration, should have a fun interface.
Should not have
• Should not have a complicated and overcrowded or jumbled up layout.

```html
<!DOCTYPE html>
<html lang="en">
<head>
<meta charset="utf-8">
<title>Valtor Holidays</title>
<link href="https://fonts.googleapis.com/css2?family=Open+Sans:ital,wght@0,400;0,600;0,700;1,400&family=Raleway:wght@400;500;600;700&display=swap" rel="stylesheet">
<style>
:root{
  --red:#cc1d2c;
  --red-dark:#a9121f;
  --red-light:#e0323c;
  --orange:#e48b10;
  --cyan:#1db2d2;
  --ink:#222;
  --text:#555;
  --muted:#888;
  --grey-band:#ebebeb;
  --footer:#0d0d0d;
  --footer-base:#151515;
  --white:#fff;
}
*{margin:0;padding:0;box-sizing:border-box}
html,body{width:1200px;height:2880px;overflow:hidden;background:var(--white)}
body{position:relative;font-family:"Open Sans",Arial,sans-serif;color:var(--text)}
.abs{position:absolute}
h1,h2,h3,h4{font-family:"Raleway",Arial,sans-serif;font-weight:500}

/* header */
.site-header{left:0;top:0;width:1200px;height:104px;background:var(--white)}
.brand{left:134px;top:30px;display:flex;align-items:center;gap:12px}
.brand-dot{width:40px;height:40px;border-radius:50%;background:var(--red)}
.brand-name{font-family:"Raleway",sans-serif;font-weight:700;font-size:30px;color:var(--red)}
.contact-top{right:126px;top:38px;text-align:right;font-size:15px;color:#333;line-height:24px}
.contact-top svg{vertical-align:-2px;margin-right:4px}

/* nav */
.main-nav{left:0;top:104px;width:1200px;height:52px;background:linear-gradient(#d62a34,var(--red-dark))}
.main-nav a{position:absolute;top:17px;color:var(--white);text-decoration:none;font-family:"Raleway",sans-serif;font-weight:600;font-size:16px;letter-spacing:.3px}

/* hero */
.hero{left:0;top:156px;width:1200px;height:526px;background:linear-gradient(100deg,#c9a27e 0%,#e7cdb0 30%,#d9c2a9 55%,#b6cddb 80%,#8fb5cc 100%)}
.slide-arrow{width:35px;height:104px;background:rgba(0,0,0,.75);display:flex;align-items:center;justify-content:center}
.booking{left:747px;top:238px;width:342px;height:363px;background:rgba(20,20,20,.88);padding:24px 33px}
.booking h3{color:var(--white);font-size:27px;font-weight:500;margin-bottom:12px}
.booking label{display:block;color:var(--white);font-size:15px;margin:10px 0 6px}
.field{height:36px;background:var(--white);border:1px solid #ccc;font-size:11px;color:#888;padding:10px 10px;position:relative}
.field svg{position:absolute;right:8px;top:10px}
.pair{display:flex;gap:8px}
.pair>div{flex:1}
.search-btn{margin-top:14px;height:42px;background:var(--cyan);color:var(--white);font-weight:700;font-size:17px;text-align:center;line-height:42px}

/* about */
.about{left:0;top:682px;width:1200px;height:272px;text-align:center}
.about h2{margin-top:50px;font-size:38px;color:#333;font-weight:400}
.about p{width:910px;margin:14px auto 0;font-size:11.5px;line-height:19px;color:#555}
.about p+p{margin-top:10px}

/* highlights */
.highlights{left:0;top:954px;width:1200px;height:371px;background:var(--grey-band);border-top:1px solid #ccc}
.hl-card{top:52px;width:302px;text-align:center}
.hl-photo{height:140px}
.hl-card h3{color:var(--red);font-size:20px;margin-top:16px}
.hl-card p{font-size:11px;line-height:16px;color:#555;margin-top:6px;padding:0 4px}
.hl-card .more{display:block;font-size:13px;color:#333;margin-top:6px}

/* tours band */
.tours{left:0;top:1325px;width:1200px;height:428px;background:linear-gradient(#5d8fbf 0%,#8bb3d6 28%,#3d6b4a 45%,#1f8a94 70%,#146c80 100%)}
.tours h2{position:absolute;top:42px;width:100%;text-align:center;color:var(--white);font-size:34px;font-weight:400}
.tour-card{top:117px;width:285px;height:263px;background:var(--white);padding:8px 0 0}
.tour-card .photo{height:153px;margin:0 4px}
.tour-info{position:absolute;left:0;right:0;bottom:0;height:102px;padding:14px 18px;color:var(--white)}
.tour-info h4{font-family:"Open Sans",sans-serif;font-weight:400;font-size:21px}
.tour-info p{font-size:11px;line-height:16px;margin-top:4px;width:170px}
.tour-info .days{position:absolute;right:20px;bottom:26px;font-size:14px;font-weight:600}

/* features */
.features{left:0;top:1753px;width:1200px;height:518px}
.features h2{position:absolute;top:62px;width:100%;text-align:center;font-size:32px;color:#333;font-weight:400}
.rule{top:84px;height:4px;background:#e5e5e5}
.feature{top:160px;width:300px;text-align:center}
.feature .icon{width:104px;height:104px;margin:0 auto;border:3px solid #d8d8d8;border-radius:50%;display:flex;align-items:center;justify-content:center}
.feature h3{font-size:24px;color:#222;margin-top:22px}
.feature p{font-size:11.5px;line-height:18px;color:#555;margin:10px auto 0;width:240px}
.feature .btn{display:inline-block;margin-top:16px;width:116px;height:38px;border:2px solid #222;line-height:34px;font-size:14px;color:#222}

/* testimonial */
.testimonial{left:0;top:2271px;width:1200px;height:298px;background:linear-gradient(#c9262e,#d8434a 60%,#c3232c)}
.notch{left:566px;top:-1px}
.testimonial h2{position:absolute;top:70px;width:100%;text-align:center;color:var(--white);font-size:28px;font-weight:500;letter-spacing:.5px}
.testimonial blockquote{position:absolute;left:290px;top:133px;width:620px;text-align:center;color:var(--white);font-style:italic;font-size:12px;line-height:19px}
.quote-mark{font-family:Georgia,serif;font-size:42px;color:var(--white);font-style:normal}
.testimonial cite{position:absolute;top:212px;width:100%;text-align:center;font-style:normal;color:var(--white);font-size:15px}

/* footer */
.site-footer{left:0;top:2569px;width:1200px;height:177px;background:var(--footer)}
.f-col{top:46px}
.f-col h4{color:var(--white);font-size:20px;font-weight:400;margin-bottom:16px}
.f-col li{list-style:none;font-size:12px;color:#bbb;line-height:23px}
.badge{width:76px;height:34px;background:#e9e9e9}
.footer-base{left:0;top:2746px;width:1200px;height:134px;background:var(--footer-base)}
.copyright{left:127px;top:74px;font-size:11px;color:#3c3c3c}
.socials{left:970px;top:70px;display:flex;gap:12px}
.socials span{width:20px;height:20px;border-radius:50%;background:#666}
</style>
</head>
<body>

<header class="site-header abs">
  <div class="brand abs"><span class="brand-dot"></span><span class="brand-name">Valtor Holidays</span></div>
  <div class="contact-top abs">
    <div><svg width="14" height="14" viewBox="0 0 24 24"><path fill="#333" d="M6.6 10.8a15 15 0 0 0 6.6 6.6l2.2-2.2c.3-.3.7-.4 1-.2 1.1.4 2.3.6 3.6.6.6 0 1 .4 1 1V20c0 .6-.4 1-1 1A17 17 0 0 1 3 4c0-.6.4-1 1-1h3.5c.6 0 1 .4 1 1 0 1.3.2 2.5.6 3.6.1.3 0 .7-.2 1z"/></svg><span style="font-size:17px">00-60391234567</span></div>
    <div>tours@valtorholidays-example.com.my</div>
  </div>
</header>

<nav class="main-nav abs">
  <a style="left:152px">HOME</a>
  <a style="left:248px">ABOUT US</a>
  <a style="left:378px">TOURS</a>
  <a style="left:480px">PAY BILLS</a>
  <a style="left:607px">OUR PACKAGES</a>
  <a style="left:777px">NEWS &amp; BLOGS</a>
  <a style="left:947px">CONTACT US</a>
</nav>

<section class="hero abs" role="img" aria-label="Photo of a young child in a sun hat playing in the sand on a sunny beach">
  <div class="slide-arrow abs" style="left:0;top:174px"><svg width="14" height="28" viewBox="0 0 14 28"><path d="M12 2 2 14l10 12" stroke="#fff" stroke-width="2" fill="none"/></svg></div>
  <div class="slide-arrow abs" style="right:0;top:174px"><svg width="14" height="28" viewBox="0 0 14 28"><path d="M2 2l10 12L2 26" stroke="#fff" stroke-width="2" fill="none"/></svg></div>
</section>

<form class="booking abs">
  <h3>Book Your Holidays</h3>
  <label>Destination</label>
  <div class="field">City, region or keyword</div>
  <div class="pair">
    <div><label>Departure</label><div class="field">Departure date<svg width="16" height="16" viewBox="0 0 16 16"><rect x="1" y="2" width="14" height="13" fill="none" stroke="#bbb"/><path d="M1 6h14" stroke="#bbb"/></svg></div></div>
    <div><label>Arrival</label><div class="field">Arrival date<svg width="16" height="16" viewBox="0 0 16 16"><rect x="1" y="2" width="14" height="13" fill="none" stroke="#bbb"/><path d="M1 6h14" stroke="#bbb"/></svg></div></div>
  </div>
  <label>Max Budgets</label>
  <div class="field">USD EX 100</div>
  <div class="search-btn">SEARCH</div>
</form>

<section class="about abs">
  <h2>Little About Malaysia Tab</h2>
  <p>Malaysia is a country blessed with beautiful natural beaches and islands, as she is made up of a large peninsular and the third largest island in the world. As Malaysia has a long history of civilisation and colonialisation, you can find traces of Portuguese, Dutch, English and Japanese architectural and cultural heritage in Malaysia.</p>
  <p>You must also visit Malaysia if you want to taste different kinds of oriental cuisine because here in Malaysia we have Malay, Chinese, Indian and a lot of other types of cuisines. Malaysia is also a must-visit place for those who want see different culture and religious practices in a harmonious community. We have some of the most beautiful mosques, largest Hindu temple complexand several gigantic Buddha monuments.</p>
</section>

<section class="highlights abs">
  <svg class="abs" style="left:56px;top:160px" width="22" height="56" viewBox="0 0 22 56"><path d="M20 2 2 28l18 26" stroke="#555" stroke-width="2" fill="none"/></svg>
  <svg class="abs" style="left:1120px;top:160px" width="22" height="56" viewBox="0 0 22 56"><path d="M2 2l18 26L2 54" stroke="#555" stroke-width="2" fill="none"/></svg>
  <article class="hl-card abs" style="left:126px">
    <div class="hl-photo" role="img" aria-label="Night view of an illuminated mosque" style="background:linear-gradient(#1a1f3a,#3b2a3a 60%,#b4722c)"></div>
    <h3>Architecture</h3>
    <p>The architecture all around Malaysia today displays almost every imaginable architectural category andstyle of Asia's main cultures and religions. Yet while the old architectural</p>
    <span class="more">Read More</span>
  </article>
  <article class="hl-card abs" style="left:449px">
    <div class="hl-photo" role="img" aria-label="Island resort huts beside a turquoise lagoon" style="background:linear-gradient(#8fb8cf,#3f6c4a 45%,#23a7b8)"></div>
    <h3>Beaches &amp; Islands</h3>
    <p>Malaysia a land of friendly people and a nation blessed with natural wonders, welcome you are bordered by Thailand to the north and Singapore to the south,</p>
    <span class="more">Read More</span>
  </article>
  <article class="hl-card abs" style="left:772px">
    <div class="hl-photo" role="img" aria-label="Floating mosque by the sea under a cloudy sky" style="background:linear-gradient(#9fb2c2,#cfd6dc 50%,#6f8a99)"></div>
    <h3>Cultural</h3>
    <p>In Malaysia, visitors will be surprised to find all of Asia's main ethnic groups living together in harmony. Indeed, all the world's major religions</p>
    <span class="more">Read More</span>
  </article>
</section>

<section class="tours abs" role="img" aria-label="Tropical coastline with green hills, clear water and a wooden jetty">
  <h2>Why Choose Us</h2>
  <svg class="abs" style="left:56px;top:160px" width="20" height="54" viewBox="0 0 20 54"><path d="M18 2 2 27l16 25" stroke="#fff" stroke-width="2" fill="none"/></svg>
  <svg class="abs" style="left:1120px;top:160px" width="20" height="54" viewBox="0 0 20 54"><path d="M2 2l16 25L2 52" stroke="#fff" stroke-width="2" fill="none"/></svg>
  <article class="tour-card abs" style="left:159px;border-top:6px solid var(--red)">
    <div class="photo" role="img" aria-label="Beach loungers and parasols under a tree" style="background:linear-gradient(#7fb0d8,#d9d2c0)"></div>
    <div class="tour-info" style="background:var(--red)"><h4>Cras ante vitae enim</h4><p>Nulla sit amet diam Duis non nunc Nulla rhon cus</p><span class="days">10 DAYS</span></div>
  </article>
  <article class="tour-card abs" style="left:463px;border-top:6px solid var(--orange)">
    <div class="photo" role="img" aria-label="Green island and turquoise bay" style="background:linear-gradient(#5c9bd0,#2f6a3c 50%,#20b3a6)"></div>
    <div class="tour-info" style="background:var(--orange)"><h4>Cras ante vitae enim</h4><p>Nulla sit amet diam Duis non nunc Nulla rhon cus</p><span class="days">08 DAYS</span></div>
  </article>
  <article class="tour-card abs" style="left:766px;border-top:6px solid var(--cyan)">
    <div class="photo" role="img" aria-label="City skyline with towers and a heritage building" style="background:linear-gradient(#4e7fb8,#8aa4bf 50%,#7a5a40)"></div>
    <div class="tour-info" style="background:var(--cyan)"><h4>Cras ante vitae enim</h4><p>Nulla sit amet diam Duis non nunc Nulla rhon cus</p><span class="days">04 DAYS</span></div>
  </article>
</section>

<section class="features abs">
  <div class="rule abs" style="left:184px;width:272px"></div>
  <div class="rule abs" style="left:730px;width:352px"></div>
  <h2>Why Choose Us</h2>
  <article class="feature abs" style="left:142px">
    <div class="icon"><svg width="44" height="44" viewBox="0 0 24 24"><path fill="var(--red)" d="M22 2 2 10l7 3 2 8 3-6 6 4z"/></svg></div>
    <h3>Our Aim</h3>
    <p>Help our trade partners sell better than their competitors and our travel clients with a memorable trip</p>
    <span class="btn">Read More</span>
  </article>
  <article class="feature abs" style="left:451px">
    <div class="icon"><svg width="44" height="44" viewBox="0 0 24 24"><circle cx="12" cy="12" r="10" fill="var(--red)"/><path d="M7 7c2 0 3 2 5 2s1 3-1 3-2 3-4 2m9-6c1 2 3 3 2 6" stroke="#fff" stroke-width="1.6" fill="none"/></svg></div>
    <h3>Price &amp; Quality</h3>
    <p>Help our trade partners sell better than their competitors and our travel clients with a memorable trip</p>
    <span class="btn">Read More</span>
  </article>
  <article class="feature abs" style="left:752px">
    <div class="icon"><svg width="44" height="44" viewBox="0 0 24 24"><circle cx="12" cy="12" r="10" fill="var(--red)"/><path d="M7 12l3.5 3.5L17 9" stroke="#fff" stroke-width="2.4" fill="none"/></svg></div>
    <h3>Tour Fleet</h3>
    <p>For sightseeing or shopping, for touring or for transfers – Valtor Holidays has just the vehicle for you.</p>
    <span class="btn">Read More</span>
  </article>
</section>

<section class="testimonial abs" role="img" aria-label="Silhouettes of people jumping against a red sky">
  <svg class="notch abs" width="68" height="22" viewBox="0 0 68 22"><path d="M0 0h68L34 22z" fill="#fff"/></svg>
  <h2>WHAT OUR CUSTOMER SAYS</h2>
  <svg class="abs" style="left:186px;top:118px" width="24" height="64" viewBox="0 0 24 64"><path d="M22 2 2 32l20 30" stroke="rgba(255,255,255,.7)" stroke-width="2" fill="none"/></svg>
  <svg class="abs" style="left:966px;top:118px" width="24" height="64" viewBox="0 0 24 64"><path d="M2 2l20 30L2 62" stroke="rgba(255,255,255,.7)" stroke-width="2" fill="none"/></svg>
  <blockquote><span class="quote-mark">“</span> Morbi diam mauris viverra in gravida eu mattis in ante Morbi eget arcu Morbi porta libero id ullamcorper non-ummy nibh ligula pulvinar metus eget consectetuer augue nisi quis lacus Ut ac mi quis lacus mollis aliquam Cura-bitur iaculis tempus eros Curabitur vel mi sit amet Mauris vel lacus vitae felis <span class="quote-mark">”</span></blockquote>
  <cite>By Author Name, City Location</cite>
</section>

<footer class="site-footer abs">
  <div class="f-col abs" style="left:127px"><h4>Company</h4><ul><li>About Company</li><li>What We Do</li><li>Our Packaage</li><li>Special Offers</li></ul></div>
  <div class="f-col abs" style="left:311px"><h4>Resources</h4><ul><li>Testimonials</li><li>News &amp; Blog</li><li>Support</li><li>Gallery</li></ul></div>
  <div class="f-col abs" style="left:492px"><h4>Support</h4><ul><li>Term of Use</li><li>Contact Us</li><li>Sitemap</li></ul></div>
  <div class="f-col abs" style="left:653px"><h4>Contact Us</h4><ul><li>Suite No. 4-02 , 4th Floor Wisma Kenanga No.21</li><li>Jalan Melati Kuala Lumpur . Malaysia</li><li>Phone: 00-60391234568</li><li>Email: tours@valtorholidays-example.com.my</li></ul></div>
  <div class="badge abs" style="left:960px;top:88px"></div>
  <div class="badge abs" style="left:966px;top:132px;width:66px"></div>
</footer>

<div class="footer-base abs">
  <p class="copyright abs">© 2015 Company Name. All right reserved. Term of Use</p>
  <div class="socials abs"><span></span><span></span><span></span><span></span></div>
</div>

</body>
</html>
```